Web Design Project for SEARCH ENGINE !

We need a website design for torrents search engine.

The Website will be www.Qurvex.com

Qurvex is a a search engine for torrents.
Qurvex search and index torrents results from all torrents sites.

We will need:
Logo
WebSite Design
slogen (optional)

we need only PSDs - no codded pages are needed !

Design to the following screen Size & resolution: 1024 x 768

***PLEASE DOWNLOAD ATTACHED FILE !

```html
<!DOCTYPE html>
<html lang="en">
<head>
<meta charset="utf-8">
<title>Qurvex – torrent meta-search</title>
<link rel="stylesheet" href="https://fonts.googleapis.com/css2?family=Open+Sans:ital,wght@0,400;0,600;0,700;1,700&display=swap">
<style>
:root{
  --navy:#0d3a64;
  --navy-dark:#092c4d;
  --band:#134c7d;
  --sky:#1ea0e2;
  --sky-light:#4cb8ee;
  --row-a:#7fd2f2;
  --row-b:#c6ebfa;
  --row-line:#5aa9cf;
  --ink:#1c2b3a;
  --link:#2a6aa0;
  --green:#1f9e3a;
  --blue-num:#1a3fd0;
  --footer:#eef1f5;
  --white:#ffffff;
}
*{box-sizing:border-box;margin:0;padding:0}
html,body{width:1090px;height:1200px;overflow:hidden;background:var(--white)}
body{font-family:"Open Sans",Arial,sans-serif;color:var(--ink);position:relative}

.site-header{position:absolute;left:0;top:0;width:1090px;height:75px;
  background:linear-gradient(var(--navy),var(--navy-dark));display:flex;align-items:center}
.brand{display:flex;align-items:center;gap:12px;margin-left:41px;width:165px;height:75px;border-right:1px solid #1e5384}
.brand-dot{width:44px;height:44px;border-radius:50%;background:var(--sky-light)}
.brand-name{color:var(--white);font-weight:700;font-size:26px}
.tagline{margin-left:26px;color:var(--white);font-style:italic;font-weight:700;font-size:25px}
.main-nav{position:absolute;right:0;top:0;height:75px;display:flex}
.main-nav a{color:var(--white);text-decoration:none;font-weight:700;font-size:16px;
  padding:0 22px;line-height:75px;border-left:1px solid #1e5384}

.search-band{position:absolute;left:0;top:75px;width:1090px;height:157px;
  background:radial-gradient(ellipse at center,var(--sky-light),var(--sky) 70%)}
.search-box{position:absolute;left:249px;top:41px;width:589px;height:71px;border-radius:36px;
  background:var(--white);border:6px solid var(--navy);box-shadow:0 0 0 2px #68c4f0}
.search-query{position:absolute;left:37px;top:18px;font-size:16px;color:var(--ink)}
.search-button{position:absolute;right:4px;top:3px}

.intro-band{position:absolute;left:0;top:232px;width:1090px;height:79px;background:var(--band)}
.intro-text{position:absolute;left:60px;top:15px;width:640px;color:var(--white);font-size:17px;line-height:24px}
.intro-text strong{font-style:italic;font-size:21px}
.like-badge{position:absolute;left:875px;top:28px;width:46px;height:26px;border-radius:3px;
  background:linear-gradient(#ffffff,#dfe6ee);border:1px solid #9fb3c8}
.like-count{position:absolute;left:935px;top:26px;width:74px;height:30px;border-radius:4px;
  background:var(--white);font-size:14px;font-weight:700;text-align:center;line-height:30px;color:var(--navy)}

.promo{position:absolute;left:0;top:311px;width:1090px;height:184px;background:var(--white)}
.promo-name{position:absolute;left:32px;top:77px;display:flex;align-items:center;gap:8px;
  font-size:24px;font-weight:600;color:var(--navy)}
.promo-name i{display:block;width:16px;height:16px;border-radius:50%;background:var(--navy)}
.promo-banner{position:absolute;left:225px;top:27px;width:831px;height:125px;
  background:linear-gradient(90deg,#f4f4f2,#e6e6e3 80%,#8cc440 80%,#7ab536)}

.results-bar{position:absolute;left:0;top:495px;width:1090px;height:40px;background:var(--navy);
  color:var(--white);font-size:16px}
.results-count{position:absolute;left:60px;top:9px}
.results-order{position:absolute;right:65px;top:9px}
.results-order a,.filter-bar a{color:#5fc2f2;text-decoration:none}
.results-order a.on{color:var(--white)}
.filter-bar{position:absolute;left:0;top:535px;width:1090px;height:47px;background:var(--sky);
  color:var(--white);font-size:16px}
.filter-bar .inner{position:absolute;right:65px;top:12px}
.filter-bar a{color:var(--white)}
.filter-bar a.on{color:var(--navy)}
.filter-bar .sep{margin:0 22px}

.results-table{position:absolute;left:60px;top:605px;width:950px;border-collapse:collapse;font-size:15.5px}
.results-table tr{height:27.6px;border-bottom:1px solid var(--row-line)}
.results-table tr:nth-child(odd){background:var(--row-a)}
.results-table tr:nth-child(even){background:var(--row-b)}
.results-table td{padding:0;white-space:nowrap}
.title{padding-left:2px!important;color:var(--ink)}
.title small{font-size:14px;color:#3e5d73}
.age{width:117px}
.size{width:94px}
.seeds{width:48px;color:var(--green)}
.peers{width:30px;color:var(--blue-num)}

.related{position:absolute;left:62px;top:928px;width:960px;font-size:14.6px;line-height:20px;color:var(--link)}
.index-stats{position:absolute;left:0;top:1007px;width:1090px;text-align:center;font-size:15px}
.divider{position:absolute;left:268px;top:1044px;width:555px;border-top:1px dashed #8a8a8a}
.categories-title{position:absolute;left:0;top:1052px;width:1090px;text-align:center;
  font-size:26px;font-weight:700;font-style:italic;color:var(--navy)}
.categories{position:absolute;left:0;top:1087px;width:1090px;text-align:center;font-size:15.5px}
.categories a{color:var(--ink)}

.site-footer{position:absolute;left:0;top:1153px;width:1090px;height:47px;background:var(--footer);
  font-size:14px;font-weight:700;color:var(--navy)}
.site-footer .copy{position:absolute;left:34px;top:14px}
.site-footer .legal{position:absolute;right:34px;top:14px}
.site-footer a{color:var(--navy);text-decoration:none}
</style>
</head>
<body>
<header class="site-header">
  <div class="brand"><span class="brand-dot"></span><span class="brand-name">Qurvex</span></div>
  <div class="tagline">Download all what you want...</div>
  <nav class="main-nav"><a href="#">Search</a><a href="#">Qurvex</a><a href="#">Profile</a><a href="#">Help</a></nav>
</header>

<section class="search-band">
  <div class="search-box">
    <span class="search-query">Motor Lane 2011</span>
    <svg class="search-button" width="52" height="52" viewBox="0 0 52 52" aria-label="Search">
      <circle cx="26" cy="26" r="25" fill="#0d3a64"/>
      <circle cx="26" cy="26" r="21" fill="#2b8fd6"/>
      <path d="M18 13h12l6 6v20H18z" fill="#fff"/>
      <path d="M30 13v6h6" fill="#cfe3f3"/>
      <path d="M27 28l6 6-6 6" fill="none" stroke="#6cbf3a" stroke-width="3"/>
    </svg>
  </div>
</section>

<section class="intro-band">
  <p class="intro-text"><strong>Qurvex</strong> is a free, fast &amp; powerful meta-search engine combining results from dozens of torrent search engines</p>
  <span class="like-badge"></span>
  <span class="like-count">37.3 K</span>
</section>

<section class="promo">
  <div class="promo-name"><i></i>Brightforge</div>
  <div class="promo-banner" role="img" aria-label="Advertising banner: win $1,000 by writing a blog post, with enter now button"></div>
</section>

<div class="results-bar">
  <span class="results-count">1-10 of 10 for “Motor Lane 2011”</span>
  <span class="results-order">order by <a href="#">relevance</a> | <a href="#">date</a> | <a href="#">Size</a> | <a class="on" href="#">peers</a></span>
</div>
<div class="filter-bar"><div class="inner">Quality: <a class="on" href="#">all</a> | <a href="#">good</a> | <a href="#">verified</a><span class="sep"></span>Search: <a href="#">filename</a> | <a class="on" href="#">Titles</a></div></div>

<table class="results-table">
  <tr><td class="title">Motor Lane 2011 07 10 <small>» tv hd television series shows video highres</small></td><td class="age">28 days ago</td><td class="size">1491 Mb</td><td class="seeds">440</td><td class="peers">30</td></tr>
  <tr><td class="title">Motor Lane 2011 07 10 <small>» tv hd television series shows video highres</small></td><td class="age">28 days ago</td><td class="size">1491 Mb</td><td class="seeds">440</td><td class="peers">30</td></tr>
  <tr><td class="title">Motor Lane 2011 07 10 <small>» tv hd television series shows video highres</small></td><td class="age">28 days ago</td><td class="size">1491 Mb</td><td class="seeds">440</td><td class="peers">30</td></tr>
  <tr><td class="title">Motor Lane 2011 07 10 <small>» tv hd television series shows video highres</small></td><td class="age">28 days ago</td><td class="size">1491 Mb</td><td class="seeds">440</td><td class="peers">30</td></tr>
  <tr><td class="title">Motor Lane 2011 07 10 <small>» tv hd television series shows video highres</small></td><td class="age">28 days ago</td><td class="size">1491 Mb</td><td class="seeds">440</td><td class="peers">30</td></tr>
  <tr><td class="title">Motor Lane 2011 07 10 <small>» tv hd television series shows video highres</small></td><td class="age">28 days ago</td><td class="size">1491 Mb</td><td class="seeds">440</td><td class="peers">30</td></tr>
  <tr><td class="title">Motor Lane 2011 07 10 <small>» tv hd television series shows video highres</small></td><td class="age">28 days ago</td><td class="size">1491 Mb</td><td class="seeds">440</td><td class="peers">30</td></tr>
  <tr><td class="title">Motor Lane 2011 07 10 <small>» tv hd television series shows video highres</small></td><td class="age">28 days ago</td><td class="size">1491 Mb</td><td class="seeds">440</td><td class="peers">30</td></tr>
  <tr><td class="title">Motor Lane 2011 07 10 <small>» tv hd television series shows video highres</small></td><td class="age">28 days ago</td><td class="size">1491 Mb</td><td class="seeds">440</td><td class="peers">30</td></tr>
  <tr><td class="title">Motor Lane 2011 07 10 <small>» tv hd television series shows video highres</small></td><td class="age">28 days ago</td><td class="size">1491 Mb</td><td class="seeds">440</td><td class="peers">30</td></tr>
</table>

<p class="related">motor lane, motor lane s17, motor lane us, motor lane s16, motor lane 720, motor lane 720p<br>
Chorale.S02E15.HDTV 2s, tidewalker 2011 2s, hot mom 3s, corsairs of the coral sea on distant tides 0s, nilo ferraz 3s, beat studio 2s,<br>
Late Arrival (2010) 2s, bastion s03 3s, dvdrip pl movies 3s, Drifter 2010 3s, crown the hour 3s, the reset office 720p 2s</p>

<p class="index-stats">Indexing 15, 337, 488 active torrents from 60, 307, 316 pages on 33 domains</p>
<div class="divider"></div>
<h2 class="categories-title">Popular Categories:</h2>
<p class="categories"><a href="#">Games</a> | <a href="#">Movies</a> | <a href="#">E-Books</a> | <a href="#">Songs</a> | <a href="#">Softwares</a></p>

<footer class="site-footer">
  <span class="copy">Copyright 2011 Qurvex &nbsp;|&nbsp; All Rights Reserved</span>
  <span class="legal"><a href="#">Privacy Policy</a> &nbsp;|&nbsp; <a href="#">Legal</a> &nbsp;|&nbsp; <a href="#">Contact Us</a></span>
</footer>
</body>
</html>
```